Emerging Education Provider Needs a Contemporary and Compelling Promotional Presentation

We are Juniper Learning and Skills Institute, a privately owned institution that is really going places. We offer a range of Diploma, Language and Short courses for both Domestic and International students with both face to face delivery and on-line or blended. We currently run out of two campuses in Brisbane (Queensland Australia) one in the heart of the city and one in the multi-cultural precinct of Bellhaven Rise. We are currently expanding with additional campuses planned for the Gold Coast and for Melbourne, Victoria.
Please refer to our web site jlsi-example.edu.au.
We need a promotional presentation (doesn't necessarily have to be in PowerPoint) to promote our business - It really needs to pop!
Proposed Pack:
Opening slide
Content & Agenda
CEO Welcome
Mission and Vision
Our Values
Why Choose JLSI (multiple slides)
Our Campuses (Brisbane, Bellhaven Rise, In Development)
Life in Brisbane (2 slides - Queensland and Brisbane)
Our Courses (3 slides - Domestic, International, On-Line)
Student Services (multiple slides)
How to Apply
Closing Slide
Updates

Reason: I will be travelling and unable to review submissions until early next week. Can all submissions please ensure the pack has a real wow factor. This will be a pack that we will have on a big screen at a trade show where thousands of people are walking by. The presentation needs to get people to stop and watch. So no graphs or data, few words per slide, lots of compelling images, a real contemporary feel.

Target Market(s)

Educational institutions, prospective students, Business to Business, seminars and trade shows.

Industry/Entity Type

Education

Font styles to use
Sans Serif

Colors
a54499

Requirements
Must have
• Consistent with our branding theme / colours.
• Template + content using information from our International Prospectus and web site.
• Delineation between domestic and international offerings.
• Showcasing the beautiful location from which we operate.
Nice to have
• Ability to utilise the presentation for generation of other marketing collateral (flyers, posters) in future.
• Cut in video footage of our location (Queensland, Brisbane, Gold Coast).
• Any general content / slides / video that may inspire travel to Australia to study or participation in study.
Should not have
• Be off-brand.

```html
<!DOCTYPE html>
<html lang="en">
<head>
<meta charset="utf-8">
<title>JLSI Promotional Presentation</title>
<link href="https://fonts.googleapis.com/css2?family=Montserrat:wght@400;500;600;700;800&display=swap" rel="stylesheet">
<style>
:root{
  --brand:#a54499;
  --brand-deep:#7a2f73;
  --brand-soft:#c98bc2;
  --ink:#2b2b33;
  --muted:#6d6d78;
  --paper:#ffffff;
  --sheet:#eef0f3;
  --sky:#5fa6e0;
  --sea:#1f7fa8;
  --sand:#e8d9b5;
  --leaf:#4f7a3e;
  --night:#141a2c;
}
*{box-sizing:border-box;margin:0;padding:0}
html,body{width:1200px;height:3600px;overflow:hidden;background:var(--sheet)}
body{font-family:"Montserrat",Arial,sans-serif;color:var(--ink)}
.deck{width:1200px;height:3600px;padding:6px;display:grid;grid-template-columns:1fr 1fr;grid-template-rows:repeat(11,1fr);gap:8px}
.slide{position:relative;overflow:hidden;background:var(--paper)}
.photo{position:absolute;inset:0}
.photo.left-half{right:55%}
.photo.right-half{left:42%}
.photo.left-part{right:60%}
.brand{display:inline-flex;align-items:center;gap:10px;font-weight:800;color:var(--brand);letter-spacing:1px}
.brand .dot{width:14px;height:14px;border-radius:50%;background:var(--brand)}
.brand.light{color:#fff}
.brand.light .dot{background:#fff}
.title{font-weight:700;color:var(--brand);font-size:17px;letter-spacing:.5px;text-transform:uppercase}
.title.light{color:#fff}
.sub{font-size:9px;letter-spacing:1px;text-transform:uppercase;color:var(--muted);font-weight:600}
.sub.light{color:#fff}
.list{list-style:none;font-size:8.5px;line-height:1.7;color:#fff;font-weight:500}
.list li::before{content:"";display:inline-block;width:5px;height:5px;background:var(--brand);border-radius:50%;margin-right:6px;vertical-align:middle}
.list.dark{color:var(--ink)}
.block{position:absolute}
.panel{position:absolute;background:rgba(255,255,255,.92);padding:14px 18px}
.shade{position:absolute;inset:0;background:linear-gradient(90deg,rgba(15,20,40,.55),rgba(15,20,40,0) 60%)}

/* photo tones */
.ph-skyline{background:
  radial-gradient(ellipse 60% 30% at 50% 78%,rgba(255,190,120,.55),transparent 70%),
  linear-gradient(180deg,#1d2a4a 0%,#35507a 45%,#6a83a6 62%,#223046 78%,#0f1522 100%)}
.ph-ceo{background:
  radial-gradient(ellipse 55% 45% at 50% 80%,#f3c01e,transparent 70%),
  linear-gradient(180deg,#f4f1ec 0%,#e9e2d6 55%,#d9b348 100%)}
.ph-reader{background:
  radial-gradient(ellipse 70% 50% at 40% 40%,#efe9e2,transparent 70%),
  linear-gradient(100deg,#cfc6bb 0%,#e8e2da 50%,#8f8a87 100%)}
.ph-values{background:
  radial-gradient(ellipse 30% 60% at 85% 60%,rgba(214,70,60,.55),transparent 70%),
  radial-gradient(ellipse 25% 55% at 55% 65%,rgba(90,130,180,.5),transparent 70%),
  linear-gradient(90deg,#f3f3f1 0%,#dfe3e6 45%,#cfd4d6 100%)}
.ph-wheel{background:
  radial-gradient(ellipse 30% 45% at 75% 40%,rgba(255,255,255,.35),transparent 70%),
  linear-gradient(180deg,#3f86d0 0%,#7db6e6 45%,#b6d6ee 60%,#5f8c4a 75%,#2f4f2c 100%)}
.ph-beach{background:
  linear-gradient(118deg,#0f4d6e 0%,#1f7fa8 30%,#5bb1cc 45%,#cfe7ea 52%,#efe2c0 60%,#b99e74 80%,#6b6a5e 100%)}
.ph-citysign{background:
  radial-gradient(ellipse 80% 25% at 40% 82%,rgba(234,64,190,.9),transparent 70%),
  radial-gradient(ellipse 40% 30% at 70% 40%,rgba(80,120,220,.35),transparent 70%),
  linear-gradient(180deg,#0c1122 0%,#1d2546 55%,#4b2a66 80%,#1a1024 100%)}
.ph-park{background:
  radial-gradient(circle at 35% 50%,#a7aaad 0,#6d7276 22%,transparent 24%),
  radial-gradient(circle at 72% 38%,#b6b9bb 0,#7b8084 10%,transparent 11%),
  linear-gradient(180deg,#5f8d4e 0%,#8fb07a 35%,#c9c9c2 60%,#9a9c98 100%)}
.ph-trains{background:
  radial-gradient(ellipse 22% 30% at 22% 55%,#f2c318,transparent 70%),
  radial-gradient(ellipse 22% 30% at 58% 55%,#f2c318,transparent 70%),
  linear-gradient(180deg,#2c3440 0%,#5b6470 35%,#9a8a3a 55%,#2b2f36 80%,#15181c 100%)}
.ph-coast{background:
  linear-gradient(200deg,#4f9ddb 0%,#7fbbe6 25%,#a8b8c2 45%,#c9c2ae 55%,#2d8ab6 70%,#0f5f86 100%)}
.ph-twilight{background:
  radial-gradient(ellipse 90% 25% at 40% 85%,rgba(255,120,200,.95),transparent 70%),
  radial-gradient(ellipse 60% 40% at 60% 45%,rgba(120,150,230,.45),transparent 70%),
  linear-gradient(180deg,#2a3f8f 0%,#4d5fb3 40%,#8a59b0 70%,#5a8a3e 100%)}
.ph-shore{background:
  linear-gradient(210deg,#a8d4f0 0%,#5fa6e0 25%,#1f6fa6 50%,#3a9cc5 62%,#efe3c4 72%,#8a9a88 100%)}
.ph-desk{background:
  radial-gradient(ellipse 50% 35% at 30% 15%,#3f6fbf,transparent 70%),
  radial-gradient(ellipse 25% 30% at 85% 35%,#d7a35c,transparent 70%),
  linear-gradient(180deg,#8fb0dc 0%,#e6ebf1 45%,#f6f4f0 100%)}
.ph-group{background:
  radial-gradient(ellipse 25% 50% at 30% 55%,#d8b49a,transparent 70%),
  radial-gradient(ellipse 25% 50% at 75% 55%,#6f8fc0,transparent 70%),
  linear-gradient(180deg,#f2efea 0%,#d9c3b0 60%,#8e7360 100%)}
.ph-sofa{background:
  radial-gradient(ellipse 35% 45% at 30% 60%,#e9d9a6,transparent 70%),
  radial-gradient(ellipse 30% 30% at 20% 85%,#2a9a9a,transparent 70%),
  linear-gradient(90deg,#cfcbc6 0%,#ebe8e3 50%,#ffffff 100%)}
.ph-team{background:
  radial-gradient(ellipse 25% 40% at 85% 35%,#d56a2c,transparent 70%),
  radial-gradient(ellipse 30% 35% at 30% 75%,#3c9a5a,transparent 70%),
  linear-gradient(135deg,#c8d3da 0%,#c9a07f 55%,#6f513c 100%)}
.ph-friends{background:
  radial-gradient(ellipse 20% 45% at 80% 60%,#d6783a,transparent 70%),
  radial-gradient(ellipse 20% 45% at 25% 70%,#3a7fc2,transparent 70%),
  linear-gradient(180deg,#f6f6f6 0%,#e8dbcf 55%,#a88a73 100%)}
.ph-library{background:
  radial-gradient(ellipse 40% 50% at 65% 60%,#e9d8c4,transparent 70%),
  radial-gradient(ellipse 25% 40% at 15% 40%,#2e7a3e,transparent 70%),
  linear-gradient(180deg,#5b4638 0%,#8f735c 45%,#cfc0ae 100%)}
.ph-grads{background:
  radial-gradient(ellipse 30% 45% at 70% 45%,#9c8467,transparent 70%),
  radial-gradient(ellipse 25% 40% at 30% 55%,#6b6f7a,transparent 70%),
  linear-gradient(135deg,#23252c 0%,#3e3b42 50%,#7a6550 100%)}

/* cover */
.cover{display:flex;flex-direction:column;align-items:center;justify-content:center;gap:14px;background:linear-gradient(135deg,#fff 60%,#f4e8f2)}
.cover .brand{font-size:48px}
.cover .brand .dot{width:26px;height:26px}
.cover .tagline{font-size:10px;letter-spacing:3px;font-weight:600;color:var(--ink)}
/* agenda */
.agenda{padding:30px 34px}
.agenda ol{list-style:none;display:grid;grid-template-columns:1fr 1fr;grid-auto-flow:column;grid-template-rows:repeat(5,auto);gap:14px 30px;margin-top:22px}
.agenda li{display:flex;align-items:center;gap:10px;font-size:11px;font-weight:500}
.agenda .num{width:22px;height:22px;border-radius:50%;background:var(--brand);color:#fff;font-size:10px;font-weight:700;display:flex;align-items:center;justify-content:center}
.steps{position:absolute;left:30px;right:30px;top:130px;height:90px}
.steps svg{width:100%;height:100%}
</style>
</head>
<body>
<main class="deck">

  <section class="slide cover">
    <div class="brand"><span class="dot"></span>JLSI</div>
    <p class="tagline">JUNIPER LEARNING AND SKILLS INSTITUTE</p>
  </section>
  <section class="slide">
    <div class="photo ph-skyline" role="img" aria-label="Brisbane city skyline at dusk"></div>
    <div class="block" style="left:0;right:0;top:60px;text-align:center">
      <div class="brand light" style="font-size:34px"><span class="dot"></span>JLSI</div>
      <p class="sub light" style="margin-top:10px;letter-spacing:3px">Juniper Learning and Skills Institute</p>
    </div>
  </section>

  <section class="slide agenda">
    <h2 class="title">Our Agenda</h2>
    <ol>
      <li><span class="num">1</span>CEO Welcome</li>
      <li><span class="num">2</span>JLSI Mission &amp; Vision</li>
      <li><span class="num">3</span>JLSI Values</li>
      <li><span class="num">4</span>Why choose JLSI</li>
      <li><span class="num">5</span>Our Campuses</li>
      <li><span class="num">6</span>Life in Brisbane</li>
      <li><span class="num">7</span>Our Courses</li>
      <li><span class="num">8</span>Student Services</li>
      <li><span class="num">9</span>How to Apply</li>
    </ol>
    <div class="brand block" style="right:24px;bottom:18px;font-size:18px"><span class="dot" style="width:10px;height:10px"></span>JLSI</div>
  </section>
  <section class="slide">
    <div class="photo left-half ph-ceo" role="img" aria-label="Smiling CEO portrait in a yellow top"></div>
    <div class="block" style="left:52%;right:24px;top:100px">
      <p style="font-size:12px;font-weight:600;line-height:1.5;color:var(--ink);text-align:center">TURN DREAMS INTO REALITY AND ASPIRATIONS INTO ACHIEVED GOALS</p>
      <p style="font-size:9px;color:var(--brand);font-weight:600;margin-top:22px;text-align:right">Chief Executive</p>
    </div>
  </section>

  <section class="slide">
    <div class="photo left-part ph-reader" role="img" aria-label="Student reading a book"></div>
    <div class="block" style="left:44%;right:24px;top:40px">
      <h3 class="title" style="font-size:14px">JLSI Mission</h3>
      <p style="font-size:10px;color:var(--brand);margin-top:6px;line-height:1.4">To provide high quality education to skilled people for life</p>
      <h3 class="title" style="font-size:14px;margin-top:30px">JLSI Vision</h3>
      <p style="font-size:10px;color:var(--brand);margin-top:6px;line-height:1.4">Empowering people to be one moment of influence and supporting our local community and beyond</p>
    </div>
  </section>
  <section class="slide">
    <div class="photo ph-values" role="img" aria-label="Students smiling in a bright corridor"></div>
    <div class="block" style="left:28px;top:34px">
      <h2 class="title">Our Values</h2>
      <ul class="list dark" style="margin-top:12px">
        <li>Excellence</li><li>Integrity</li><li>Respect</li><li>Commitment</li>
      </ul>
    </div>
  </section>

  <section class="slide">
    <div class="photo ph-wheel" role="img" aria-label="Riverside Ferris wheel under a blue sky"></div>
    <div class="shade"></div>
    <div class="block" style="left:26px;top:24px">
      <h2 class="title light">Why Choose JLSI</h2>
      <ul class="list" style="margin-top:10px">
        <li>Students are our focus</li><li>We love education</li><li>Highest quality trainers</li><li>Flexibility</li><li>Modern facilities</li>
      </ul>
    </div>
  </section>
  <section class="slide">
    <div class="photo ph-beach" role="img" aria-label="Aerial view of a long sandy beach and surf"></div>
    <div class="block" style="left:28px;top:150px">
      <h2 class="title light">The JLSI Way</h2>
      <p class="sub light" style="margin-top:6px">Learn, grow and thrive</p>
    </div>
  </section>

  <section class="slide">
    <div class="photo ph-citysign" role="img" aria-label="Illuminated city sign at night"></div>
    <div class="block" style="left:26px;top:28px">
      <h2 class="title light">Our Campuses</h2>
      <p class="sub light" style="margin-top:8px">Brisbane City</p>
      <p style="font-size:8.5px;color:#fff;margin-top:6px">Level 3, 120 Harbour Street, Brisbane QLD</p>
    </div>
  </section>
  <section class="slide">
    <div class="photo ph-park" role="img" aria-label="Metal sphere sculptures in a city park"></div>
    <div class="panel" style="right:0;bottom:36px;width:52%">
      <h2 class="title">Our Campuses</h2>
      <p class="sub" style="margin-top:6px">Bellhaven Rise</p>
      <p style="font-size:8.5px;margin-top:6px;color:var(--ink)">Suite 4, 18 Orchard Lane, Bellhaven Rise QLD</p>
    </div>
  </section>

  <section class="slide">
    <div class="photo ph-trains" role="img" aria-label="Commuter trains at a city station"></div>
    <div class="panel" style="right:0;bottom:30px;width:46%">
      <h2 class="title">Our Campuses</h2>
      <p class="sub" style="margin-top:6px">Easy transport access</p>
    </div>
  </section>
  <section class="slide">
    <div class="photo ph-coast" role="img" aria-label="Coastal city towers beside the ocean"></div>
    <div class="block" style="right:28px;top:24px;text-align:right">
      <h2 class="title light">Our Campuses</h2>
      <p class="sub light" style="margin-top:6px">In development</p>
      <p style="font-size:8.5px;color:#fff;margin-top:4px">Gold Coast &amp; Melbourne</p>
    </div>
  </section>

  <section class="slide">
    <div class="photo ph-twilight" role="img" aria-label="Colourful city letters at twilight"></div>
    <div class="block" style="left:26px;top:24px">
      <h2 class="title" style="color:#f5b8e6">Life in Queensland</h2>
    </div>
    <ul class="list block" style="left:46%;top:30px">
      <li>Sunshine all year round</li><li>World class beaches</li><li>Friendly, safe cities</li><li>Rainforests and reefs</li>
    </ul>
  </section>
  <section class="slide">
    <div class="photo ph-shore" role="img" aria-label="Beachfront skyline and blue sea"></div>
    <div class="shade"></div>
    <div class="block" style="left:26px;top:90px">
      <h2 class="title light">Life in Brisbane</h2>
      <ul class="list" style="margin-top:8px">
        <li>Vibrant riverside city</li><li>Multicultural community</li><li>Affordable living</li><li>Great public transport</li><li>Close to Gold Coast</li>
      </ul>
    </div>
  </section>

  <section class="slide">
    <div class="photo ph-desk" role="img" aria-label="Student writing notes at a desk"></div>
    <div class="block" style="left:28px;bottom:24px">
      <h2 class="title">Our Courses</h2>
      <p class="sub" style="margin-top:6px;color:var(--brand)">Domestic</p>
      <ul class="list dark" style="margin-top:4px"><li>Diploma</li><li>Certificate</li><li>Short courses</li></ul>
    </div>
  </section>
  <section class="slide">
    <div class="photo right-half ph-group" role="img" aria-label="Group of international students with books"></div>
    <div class="block" style="left:26px;top:90px">
      <h2 class="title">Our Courses</h2>
      <p class="sub" style="margin-top:6px;color:var(--brand)">International</p>
      <ul class="list dark" style="margin-top:4px"><li>Business courses</li><li>General English courses</li><li>English courses</li><li>Interpreting courses</li></ul>
    </div>
  </section>

  <section class="slide">
    <div class="photo ph-sofa" role="img" aria-label="Student studying on a laptop on a sofa"></div>
    <div class="block" style="right:40px;top:70px;text-align:right">
      <h2 class="title">Our Courses</h2>
      <p class="sub" style="margin-top:6px;color:var(--brand)">Online</p>
    </div>
  </section>
  <section class="slide">
    <div class="photo ph-team" role="img" aria-label="Students collaborating around a table"></div>
    <div class="block" style="left:30%;right:26px;top:20px;padding:8px 12px;background:rgba(255,255,255,.8);text-align:center">
      <h2 class="title">Student Services</h2>
      <p class="sub" style="margin-top:4px">Support and counselling</p>
    </div>
  </section>

  <section class="slide">
    <div class="photo ph-friends" role="img" aria-label="Four students smiling together"></div>
    <div class="block" style="left:26px;top:20px">
      <h2 class="title">Student Services</h2>
      <p class="sub" style="margin-top:4px">Study help and guidance</p>
    </div>
  </section>
  <section class="slide">
    <div class="photo ph-library" role="img" aria-label="Student holding books in a library"></div>
    <div class="panel" style="left:160px;top:120px;width:44%;background:rgba(165,68,153,.85)">
      <h2 class="title light" style="font-size:15px">Student Services</h2>
      <p class="sub light" style="margin-top:4px">Career advice</p>
    </div>
  </section>

  <section class="slide">
    <h2 class="title block" style="left:28px;top:30px;color:var(--ink)">How to Apply</h2>
    <div class="steps">
      <svg viewBox="0 0 530 90" aria-label="Application steps">
        <line x1="20" y1="30" x2="510" y2="30" stroke="#a54499" stroke-width="2"/>
        <g fill="#a54499">
          <circle cx="20" cy="30" r="9"/><circle cx="142" cy="30" r="9"/><circle cx="265" cy="30" r="9"/><circle cx="388" cy="30" r="9"/><circle cx="510" cy="30" r="9"/>
        </g>
        <g font-family="Montserrat, Arial, sans-serif" font-size="8" fill="#2b2b33" text-anchor="middle">
          <text x="20" y="60">Choose</text><text x="142" y="60">Apply online</text><text x="265" y="60">Get offer</text><text x="388" y="60">Accept</text><text x="510" y="60">Enrol</text>
        </g>
      </svg>
    </div>
    <p class="block" style="left:28px;bottom:22px;font-size:9px;color:var(--brand);font-weight:600">jlsi-example.edu.au</p>
  </section>
  <section class="slide">
    <div class="photo ph-grads" role="img" aria-label="Group of graduates celebrating"></div>
    <div class="shade"></div>
    <div class="block" style="left:30px;top:30px">
      <div class="brand light" style="font-size:22px"><span class="dot" style="width:12px;height:12px"></span>JLSI</div>
      <h2 style="font-size:36px;font-weight:800;color:#fff;margin-top:80px;letter-spacing:1px">THANK YOU</h2>
    </div>
  </section>

</main>
</body>
</html>
```